Webdesign für IT-Beratungsdienstleister
Zielgruppe
7K-ADVISA ist spezialisiert auf Fach- und IT-Beratungsdienstleistungen.
Wir unterstützen Unternehmen bei der Leistungsoptimierung durch prozessgetriebene Informationssysteme und Integrationslösungen.
Bitte siehe Aufgaben hier: http://www.7k-advisa.example/ueber-uns/
Zielgruppe sind Mittelständige und sowie Grossunternehmen
Aufgabenstellung
Wordpress template, modern, nicht zu überladen mit der Möglichkeit Beiträge zu veröffentlicehn. Responsive.

```html
<!DOCTYPE html>
<html lang="de">
<head>
<meta charset="utf-8">
<title>7K-ADVISA – Über Uns</title>
<link href="https://fonts.googleapis.com/css2?family=Ubuntu:wght@300;400;500;700&family=Bree+Serif&display=swap" rel="stylesheet">
<style>
:root{
  --orange:#e8650f;
  --red:#e2351e;
  --text:#4a4a4a;
  --heading:#333;
  --footer:#273039;
  --white:#fff;
}
*{margin:0;padding:0;box-sizing:border-box}
html,body{width:747px;height:1200px;overflow:hidden}
body{position:relative;background:var(--white);font-family:'Ubuntu',sans-serif;color:var(--text)}
.abs{position:absolute}
.header{left:0;top:0;width:747px;height:39px;background:var(--white)}
.brand{left:153px;top:9px;font-size:19px;font-weight:400;color:var(--heading);letter-spacing:.5px;display:flex;align-items:center;gap:5px}
.brand .dot{width:8px;height:8px;border-radius:50%;background:var(--red)}
.nav{top:14px;left:345px;display:flex;gap:11px;font-size:6.6px;font-weight:300;color:#666}
.nav span{padding:2px 4px}
.nav .active{border:1px solid var(--orange);color:var(--orange)}
.hero{left:0;top:39px;width:747px;height:124px;background:linear-gradient(90deg,#a7a9b3,#9c9ea9 55%,#8f919c)}
.hero-sofa{left:325px;top:97px;width:211px;height:66px;background:linear-gradient(#e56d2f,#c95a20);border-radius:6px 6px 0 0}
.hero-frame{left:495px;top:47px;width:102px;height:75px;background:linear-gradient(#c8c8c8,#bcbcbc);border:4px solid #222}
.hero-title{left:150px;top:74px;font-size:15px;font-weight:500;color:var(--white)}
.rule{height:1.5px;width:20px;background:var(--red)}
h2{position:absolute;font-size:11.5px;font-weight:300;color:var(--heading)}
.para{font-size:5.8px;line-height:9.8px;font-weight:300;color:#555}
.list{list-style:none;font-size:6.3px;font-weight:300;color:#555}
.list li{height:12.6px;display:flex;align-items:flex-start;gap:4px}
.list li svg{flex:none;margin-top:1px}
.list li.wrap{height:23.5px;line-height:10.5px}
.band{left:0;top:490px;width:747px;height:146px;background:linear-gradient(90deg,#c3c5cb,#d8d9dd 45%,#eeeeee 60%,#f6f6f6)}
.band-text{left:150px;top:550px;font-size:11px;line-height:19.5px;font-weight:300;color:#444}
.slogan{left:444px;top:508px;font-family:'Bree Serif',serif;font-size:17px;line-height:25px;color:#222}
.slogan span{display:block}
.cta-bg{left:0;top:636px;width:747px;height:215px;background:linear-gradient(#8393b0,#7e8798 50%,#666b74)}
.cta{left:150px;top:701px;width:447px;height:79px;background:var(--orange);border-radius:2px}
.cta-title{left:169px;top:733px;font-size:9.5px;font-weight:300;color:var(--white)}
.cta-sub{left:169px;top:753px;font-size:5.8px;font-weight:300;color:#ffd2b3}
.cta-btn{left:506px;top:741px;width:70px;height:14px;border:1px solid var(--white);border-radius:1px;color:var(--white);font-size:5.4px;font-weight:700;display:flex;align-items:center;justify-content:center}
.map{left:0;top:851px;width:747px;height:196px;background:linear-gradient(90deg,#f6e3d4,#f7b98a 40%,#f5a775 70%,#f6d0b3)}
.footer{left:0;top:1047px;width:747px;height:153px;background:var(--footer)}
.foot-brand{left:153px;top:1066px;font-size:14px;color:var(--white);display:flex;align-items:center;gap:4px}
.foot-brand .dot{width:6px;height:6px;border-radius:50%;background:var(--white)}
.foot-text{left:150px;top:1101px;width:180px;font-size:4.2px;line-height:9.8px;font-weight:700;color:var(--white)}
.foot-h{font-size:7px;font-weight:700;color:var(--white)}
.foot-links{left:341px;top:1084px;list-style:none;font-size:4.5px;font-weight:700;color:var(--white)}
.foot-links li{height:9.9px}
.social{left:498px;top:1081px;display:flex;flex-direction:column;gap:2px}
.social span{width:12px;height:12px;background:#111;display:block}
.foot-rule{left:150px;top:1161px;width:447px;height:2px;background:var(--red)}
.copy{left:0;top:1176px;width:747px;text-align:center;font-size:5.8px;font-weight:300;color:#9aa1a9}
.copy b{color:var(--white);font-weight:500}
</style>
</head>
<body>
<svg width="0" height="0" style="position:absolute">
  <defs>
    <symbol id="tick" viewBox="0 0 10 10"><path d="M1 5.5l2.6 2.6L9 2" fill="none" stroke="#e8650f" stroke-width="2"/></symbol>
  </defs>
</svg>

<header class="abs header">
  <div class="abs brand"><span class="dot"></span>7K-ADVISA</div>
  <nav class="abs nav">
    <span>Home</span><span class="active">Über Uns</span><span>Business Consulting</span><span>IT Consulting</span><span>Training</span><span>Kontakt</span>
  </nav>
</header>

<section class="abs hero" role="img" aria-label="Foto: graue Wand mit orangefarbenem Sofa und gerahmtem Firmenschild"></section>
<div class="abs hero-sofa" role="img" aria-label="Orangefarbenes Sofa"></div>
<div class="abs hero-frame" role="img" aria-label="Bilderrahmen an der Wand"></div>
<div class="abs hero-title">Über Uns</div>
<div class="abs rule" style="left:150px;top:98px"></div>

<h2 style="left:150px;top:200px">Unsere Arbeit</h2>
<div class="abs rule" style="left:150px;top:222px"></div>
<p class="abs para" style="left:150px;top:234px;width:300px">7K-ADVISA ist spezialisiert auf Fach- und IT-Beratungsdienstleistungen.<br>Wir unterstützen Unternehmen bei der Leistungsoptimierung durch prozessgetriebene Informationssysteme.<br>Unsere Kunden vertrauen unseren Full-Service Ansatz, der sich durch hohe Expertise mit fundierten<br>Branchenübergreifenden Erfahrungen sowie Kompetenzen auszeichnet.</p>

<h2 style="left:456px;top:200px">Unsere Werte</h2>
<div class="abs rule" style="left:456px;top:222px"></div>
<p class="abs para" style="left:456px;top:234px;width:136px">Wir verpflichten uns zu einer partnerschaftlichen Arbeitsweise mit unseren Kunden sowie Stakeholder. Wir liefern stetig hochwertige Dienstleistungen.</p>

<h2 style="left:150px;top:295px">Unsere Kernaufgaben</h2>
<div class="abs rule" style="left:150px;top:317px"></div>
<h2 style="left:303px;top:295px">Unsere Kernkompetenzen</h2>
<div class="abs rule" style="left:303px;top:317px"></div>

<ul class="abs list" style="left:151px;top:332px;width:140px">
  <li><svg width="7" height="7"><use href="#tick"/></svg>Projektmanagement</li>
  <li><svg width="7" height="7"><use href="#tick"/></svg>Architekturmanagement und -beratung</li>
  <li class="wrap"><svg width="7" height="7"><use href="#tick"/></svg><span>Prozessmanagement, –beratung und -implementierung</span></li>
  <li><svg width="7" height="7"><use href="#tick"/></svg>Software Engineering</li>
  <li><svg width="7" height="7"><use href="#tick"/></svg>Professional Training und Coach</li>
</ul>
<ul class="abs list" style="left:304px;top:332px">
  <li><svg width="7" height="7"><use href="#tick"/></svg>Prozessmanagement und Optimierung</li>
  <li><svg width="7" height="7"><use href="#tick"/></svg>BPM / SOA / Business Rules</li>
  <li><svg width="7" height="7"><use href="#tick"/></svg>Business Analysis</li>
  <li><svg width="7" height="7"><use href="#tick"/></svg>Enterprise Architecture</li>
  <li><svg width="7" height="7"><use href="#tick"/></svg>Professional Training</li>
</ul>
<ul class="abs list" style="left:457px;top:332px">
  <li><svg width="7" height="7"><use href="#tick"/></svg>Digitalisierung sowie Industrie 4.0</li>
  <li><svg width="7" height="7"><use href="#tick"/></svg>API, SOA, JEE, Velmora Lösungen</li>
  <li><svg width="7" height="7"><use href="#tick"/></svg>E-Commerce, ERP, CRM Lösungen</li>
  <li><svg width="7" height="7"><use href="#tick"/></svg>Integration Lösungen</li>
</ul>

<h2 style="left:0;width:747px;text-align:center;top:406px">Unsere Branchenerfahrung</h2>
<div class="abs rule" style="left:363px;top:428px"></div>
<ul class="abs list" style="left:151px;top:443px">
  <li><svg width="7" height="7"><use href="#tick"/></svg>Banken &amp; Finanzen</li>
  <li><svg width="7" height="7"><use href="#tick"/></svg>Industrie &amp; Automotive</li>
</ul>
<ul class="abs list" style="left:304px;top:443px">
  <li><svg width="7" height="7"><use href="#tick"/></svg>Handel &amp; Logistik</li>
  <li><svg width="7" height="7"><use href="#tick"/></svg>IT Dienstleistung</li>
</ul>
<ul class="abs list" style="left:457px;top:443px">
  <li><svg width="7" height="7"><use href="#tick"/></svg>Gesundheit &amp; Public</li>
  <li><svg width="7" height="7"><use href="#tick"/></svg>Hochschulen</li>
</ul>

<section class="abs band" role="img" aria-label="Foto: helles Großraumbüro mit Stühlen und Tischen"></section>
<p class="abs band-text">Wir streben eine ständige Erweiterung<br>unserer Kernbranchen an.</p>
<div class="abs slogan">
  <span>Expertise.</span>
  <span style="margin-left:10px">Experience.</span>
  <span style="margin-left:21px">Excellence.</span>
  <span style="margin-left:32px">Consulting</span>
</div>

<section class="abs cta-bg" role="img" aria-label="Foto: Stadtpanorama mit Fernsehturm im Dunst"></section>
<div class="abs cta"></div>
<p class="abs cta-title">Wir freuen uns immer, von Ihnen zu hören.</p>
<p class="abs cta-sub">Inhaber und Ansprechpartner: Dr. Lennart Vossberg</p>
<div class="abs cta-btn">Kontakt aufnehmen</div>

<section class="abs map" role="img" aria-label="Stadtplan mit Standortmarkierung in orangefarbenen Tönen"></section>

<footer class="abs footer"></footer>
<div class="abs foot-brand"><span class="dot"></span>7K-ADVISA</div>
<p class="abs foot-text">Lorem ipsum dolor sit amet, consetetur sadipscing elitr, sed diam nonumy eirmod tempor invidunt ut labore et dolore magna aliquyam erat, sed diam voluptua. At vero eos et accusam et justo duo dolores et ea rebum.</p>
<p class="abs foot-h" style="left:341px;top:1069px">Links</p>
<ul class="abs foot-links">
  <li>Home</li><li>Über Uns</li><li>Business Consulting</li><li>IT Consulting</li><li>Training</li><li>Kontakt</li>
</ul>
<p class="abs foot-h" style="left:494px;top:1069px">Soziale Netzwerke</p>
<div class="abs social"><span></span><span></span><span></span><span></span><span></span></div>
<div class="abs foot-rule"></div>
<p class="abs copy">Copyright © 2016 7K-ADVISA. | <b>Home</b> | <b>Impressum</b> | <b>Kontakt</b></p>
</body>
</html>
```